ALL TEXT GRAPHICS TM May 2025 for Instagram

We are looking for a series of social media graphics for Instagram (new size: 4:5 (1080 x 1350 pixels) ratio that are ALL TEXT. We want the following quotes below on each graphic; one quote per graphic. AND, In very small letters at the bottom of each graphic, add @TovaMarshOnline
The look and feel of these graphics should be complimentary to the color palette attached below; but keep them simple. But the design is up to you; at the end of this document, I provided various samples of all text graphics that I like as examples.
Target Market(s)
women looking to lose weight
Look and feel

```html
<!DOCTYPE html>
<html lang="en">
<head>
<meta charset="utf-8">
<title>Hormone Reset – Instagram Text Series</title>
<link rel="stylesheet" href="https://fonts.googleapis.com/css2?family=Poppins:ital,wght@0,400;0,700;0,800;1,400&display=swap">
<style>
  :root {
    --stage: #3d2a35;
    --white: #ffffff;
    --magenta-deep: #d6066e;
    --magenta: #ff0a87;
    --pink-hot: #ff3c9c;
    --pink-mid: #ff66b0;
    --pink-soft: #ff9acb;
    --pink-pale: #ffc4df;
    --pink-bright: #ff45a3;
    --pink-vivid: #ff2a95;
    --pink-punch: #ff0f8a;
    --berry: #c8005e;
    --berry-strong: #e5007a;
  }
  * { box-sizing: border-box; margin: 0; padding: 0; }
  html, body { width: 1200px; height: 376px; overflow: hidden; }
  body {
    background: var(--stage);
    font-family: "Poppins", sans-serif;
    display: flex;
    align-items: center;
    justify-content: center;
  }
  .series { display: flex; gap: 6px; }
  .post {
    position: relative;
    width: 109.5px;
    height: 141px;
    padding: 26px 10px 0 15px;
    background: var(--bg);
    color: var(--white);
  }
  .headline {
    font-weight: 800;
    font-size: 11px;
    line-height: 0.86;
    text-transform: uppercase;
    letter-spacing: -0.1px;
  }
  .headline span { display: block; }
  .body-copy {
    margin-top: 9px;
    font-size: 6.2px;
    line-height: 1.25;
  }
  .callout {
    margin-top: 9px;
    font-weight: 700;
    font-size: 6.6px;
    letter-spacing: 1.6px;
    text-transform: uppercase;
    line-height: 1.3;
  }
  .keyword { font-weight: 700; letter-spacing: 1.2px; text-transform: uppercase; }
  .handle {
    position: absolute;
    right: 9px;
    bottom: 9px;
    font-size: 3.8px;
    font-style: italic;
  }
  .lt { color: var(--lt); }
  .dk { color: var(--dk); }
  .wh { color: var(--white); }

  .post--tired { --bg: var(--magenta-deep); --lt: #ff86c2; }
  .post--weight { --bg: var(--magenta); --dk: #e0006f; }
  .post--belly { --bg: var(--pink-hot); --lt: #ffb0d6; --dk: var(--berry); }
  .post--after40 { --bg: var(--pink-mid); --lt: #ffb8dc; --dk: #d4006a; }
  .post--flat { --bg: var(--pink-soft); --lt: #ffd0e7; --dk: var(--berry-strong); --mid: #ff5fae; }
  .post--bloat { --bg: var(--pink-pale); --lt: #ff94c8; --dk: #ff1f8f; color: #ff5fae; }
  .post--right { --bg: #ff9ccd; --lt: #ffc6e2; --dk: var(--berry-strong); }
  .post--plan { --bg: var(--pink-bright); --lt: #ff9ccd; --dk: var(--berry); }
  .post--secret { --bg: var(--pink-vivid); --lt: #ffa6d0; --dk: var(--berry); }
  .post--thirties { --bg: var(--pink-punch); --dk: #e0006f; }
  .mid { color: var(--mid); }
</style>
</head>
<body>
<main class="series">
  <article class="post post--tired">
    <h2 class="headline"><span>Tired.</span><span>Moody.</span><span class="lt">Stubborn</span><span>Belly fat.</span></h2>
    <p class="body-copy">Your hormones<br>are screaming<br>for help!</p>
    <p class="callout">Let’s fix that.</p>
    <p class="handle">@TovaMarshOnline</p>
  </article>

  <article class="post post--weight">
    <h2 class="headline"><span>That</span><span>stubborn</span><span>weight?</span><span class="dk">It’s not</span><span class="dk">your fault.</span></h2>
    <p class="body-copy">Your hormones<br>are to blame and<br>you’re not alone; but</p>
    <p class="callout">There is a fix.</p>
    <p class="handle">@TovaMarshOnline</p>
  </article>

  <article class="post post--belly">
    <h2 class="headline"><span class="lt">Your belly</span><span class="lt">isn’t fat…</span><span class="dk">It’s</span><span class="dk">hormonal.</span></h2>
    <p class="body-copy">And here’s how<br>to fix it.</p>
    <p class="body-copy" style="margin-top:6px">Comment <span class="keyword dk">Hormones</span><br>if nothing is working.</p>
    <p class="handle">@TovaMarshOnline</p>
  </article>

  <article class="post post--after40">
    <h2 class="headline"><span>The</span><span>stubborn</span><span class="dk">belly fat</span><span class="lt">after 40?</span></h2>
    <p class="body-copy">It’s not about calories;<br>it’s about your hormones.</p>
    <p class="callout dk">Here is the fix!</p>
    <p class="handle">@TovaMarshOnline</p>
  </article>

  <article class="post post--flat">
    <h2 class="headline"><span class="lt">Flat</span><span class="lt">tummy</span><span class="mid">in your 40s?</span><span class="dk">It’s still</span><span class="dk">possible!</span></h2>
    <p class="body-copy">Comment<br><span class="keyword dk">Bye belly</span><br>to get the 10 secrets<br>to a flatter tummy.</p>
    <p class="handle">@TovaMarshOnline</p>
  </article>

  <article class="post post--bloat">
    <h2 class="headline"><span class="lt">Bloating.</span><span class="dk">Muffin top.</span><span class="dk">Puffy</span><span class="dk">waistline.</span></h2>
    <p class="body-copy">Your body’s<br>screaming for a<br>different kind of fix.</p>
    <p class="callout dk">Here it is</p>
    <p class="handle">@TovaMarshOnline</p>
  </article>

  <article class="post post--right">
    <h2 class="headline"><span class="lt">You’re</span><span class="lt">doing all</span><span class="lt">the <span class="wh" style="display:inline">“right”</span></span><span class="lt">things,</span></h2>
    <p class="body-copy">but your belly<br>won’t go down?</p>
    <p class="callout dk">Here’s what<br>you haven’t tried.</p>
    <p class="handle">@TovaMarshOnline</p>
  </article>

  <article class="post post--plan" style="padding-top:20px">
    <h2 class="headline"><span class="lt">This</span><span>90-day</span><span>plan <span class="lt" style="display:inline">helped</span></span><span class="dk">women</span><span class="dk">over 40 <span class="lt" style="display:inline">slim</span></span><span class="lt">down,</span></h2>
    <p class="body-copy">get a tiny waist<br>and feel sexy again.</p>
    <p class="callout dk">You’re next.</p>
    <p class="handle">@TovaMarshOnline</p>
  </article>

  <article class="post post--secret" style="padding-top:20px">
    <h2 class="headline"><span class="lt">This is</span><span class="lt">the secret</span><span class="dk">women</span><span class="dk">over 40 <span class="lt" style="display:inline">are</span></span><span class="lt">using to get</span><span class="lt">snatched;</span><span>without</span><span>starving</span></h2>
    <p class="body-copy">Comment<br><span class="keyword dk">Skinny</span><br>to get the exact plan.</p>
    <p class="handle">@TovaMarshOnline</p>
  </article>

  <article class="post post--thirties">
    <h2 class="headline"><span>What</span><span>worked in</span><span class="dk">your 30s</span><span>won’t</span><span>work now.</span></h2>
    <p class="body-copy">Here’s what<br>actually does.<br>Drop 30 Pounds</p>
    <p class="callout">In 3 months.</p>
    <p class="handle">@TovaMarshOnline</p>
  </article>
</main>
</body>
</html>
```